Custom Truck shop New Business Card design

double sided business card including my new logo, brand colors and picking a font I attached, clean and modern look. I attached the old card for some reference. and would like to include the picture of the white truck attached. I would also like to have it with one of my employees info as well. (same info except name and title Brin Tolvay Service Writer)

Dale Porvick
Owner

address
48310 E Calloway Ridge Rd S
STE 217
Marsh Hollow, CO 80219

phone 720-555-0184

email dale@brokenspurrigs.example

website brokenspurrgis.example

social @brokenspurrigs

Target Market(s)

men 18-60

Industry/Entity Type

Automotive

Contact Information for Business Card

Dale Porvick Owner address 48310 E Calloway Ridge Rd S STE 217 Marsh Hollow, CO 80219 phone 720-555-0184 email dale@brokenspurrigs.example website brokenspurrgis.example social @brokenspurrigs

Font styles to use
Other font styles liked:
• fonts attached

Requirements
Must have
• new logo, orange #FC68D, Charcoal #333333
Nice to have
• the white truck

```html
<!DOCTYPE html>
<html lang="en">
<head>
<meta charset="utf-8">
<title>Broken Spur Rigs – Business Card</title>
<link rel="stylesheet" href="https://fonts.googleapis.com/css2?family=Montserrat:wght@500;700;800&family=Open+Sans:wght@400;600&display=swap">
<style>
  :root {
    --stage: #262626;
    --charcoal: #333333;
    --charcoal-deep: #1a1a1a;
    --orange: #f26522;
    --white: #ffffff;
    --ink: #2b2b2b;
  }
  * { box-sizing: border-box; margin: 0; padding: 0; }
  html, body { width: 1200px; height: 689px; overflow: hidden; }
  body {
    background: var(--stage);
    position: relative;
    font-family: "Open Sans", Arial, sans-serif;
  }
  .card {
    position: absolute;
    top: 190px;
    width: 540px;
    height: 309px;
    border-radius: 18px;
    overflow: hidden;
  }
  .card--back { left: 40px; background: var(--charcoal); }
  .card--front { left: 620px; background: var(--white); }

  .brand-name {
    font-family: "Montserrat", Arial, sans-serif;
    font-weight: 800;
    letter-spacing: 1px;
    text-transform: uppercase;
    white-space: nowrap;
  }
  .brand-rule { display: block; height: 2px; background: var(--orange); }

  /* back side */
  .back-pattern {
    position: absolute; inset: 0;
    background: radial-gradient(ellipse at 85% 5%, #9a9a9a 0%, #555 30%, #2e2e2e 60%, var(--charcoal-deep) 100%);
  }
  .back-brand {
    position: absolute;
    left: 0; right: 0; top: 118px;
    display: flex; align-items: center; justify-content: center; gap: 16px;
  }
  .brand-dot {
    width: 48px; height: 48px; border-radius: 50%;
    background: var(--white);
    border: 4px solid var(--orange);
    flex: none;
  }
  .back-brand .brand-name { color: var(--white); font-size: 28px; }
  .back-brand .brand-rule { margin-top: 8px; }

  /* front side */
  .front-band {
    position: absolute;
    left: 0; right: 0; bottom: 0; height: 84px;
    background: var(--charcoal);
  }
  .front-photo {
    position: absolute;
    right: 0; top: 90px;
    width: 250px; height: 219px;
    background: linear-gradient(160deg, #eceef0 0%, #c2c5c9 40%, #5d6064 78%, #2e2e2e 100%);
  }
  .front-brand {
    position: absolute; right: 26px; top: 30px;
    text-align: right;
  }
  .front-brand .brand-name { color: var(--charcoal); font-size: 20px; }
  .front-brand .brand-rule { margin-top: 6px; }

  .person { position: absolute; left: 32px; top: 92px; }
  .person-name {
    font-family: "Montserrat", Arial, sans-serif;
    font-weight: 800; font-size: 24px; color: var(--ink);
    text-transform: uppercase; letter-spacing: .5px;
    line-height: 1.1;
  }
  .person-title {
    font-family: "Montserrat", Arial, sans-serif;
    font-weight: 500; font-size: 14px; color: var(--orange);
    margin-top: 2px;
  }
  .contacts { list-style: none; position: absolute; left: 32px; top: 150px; }
  .contacts li {
    display: flex; align-items: center; gap: 10px;
    font-size: 13px; color: var(--ink); line-height: 22px;
  }
  .contacts svg { width: 13px; height: 13px; fill: var(--orange); flex: none; }
  .address {
    position: absolute; left: 32px; bottom: 13px;
    color: var(--white); font-size: 13px; line-height: 20px;
    font-style: normal;
  }
</style>
</head>
<body>

<section class="card card--back" aria-label="Card back">
  <div class="back-pattern" role="img" aria-label="Dark charcoal background with a repeating pattern of the brand emblem in glossy grey tones"></div>
  <div class="back-brand">
    <span class="brand-dot"></span>
    <div>
      <span class="brand-name">Broken Spur Rigs</span>
      <span class="brand-rule"></span>
    </div>
  </div>
</section>

<section class="card card--front" aria-label="Card front">
  <div class="front-band"></div>
  <div class="front-photo" role="img" aria-label="Photo of a lifted white pickup truck with chrome wheels"></div>

  <div class="front-brand">
    <span class="brand-name">Broken Spur Rigs</span>
    <span class="brand-rule"></span>
  </div>

  <div class="person">
    <p class="person-name">Dale Porvick</p>
    <p class="person-title">Owner</p>
  </div>

  <ul class="contacts">
    <li>
      <svg viewBox="0 0 24 24" aria-hidden="true"><path d="M6.6 10.8a15 15 0 0 0 6.6 6.6l2.2-2.2a1 1 0 0 1 1-.25 11.4 11.4 0 0 0 3.6.57 1 1 0 0 1 1 1V20a1 1 0 0 1-1 1A17 17 0 0 1 3 4a1 1 0 0 1 1-1h3.5a1 1 0 0 1 1 1c0 1.25.2 2.45.57 3.57a1 1 0 0 1-.25 1z"/></svg>
      720-555-0184
    </li>
    <li>
      <svg viewBox="0 0 24 24" aria-hidden="true"><path d="M2 5h20v14H2z"/><path d="M3 6l9 7 9-7" fill="none" stroke="#fff" stroke-width="1.6"/></svg>
      dale@brokenspurrigs.example
    </li>
    <li>
      <svg viewBox="0 0 24 24" aria-hidden="true"><circle cx="12" cy="12" r="10"/><path d="M2 12h20M12 2c3 3 3 17 0 20M12 2c-3 3-3 17 0 20M4 7h16M4 17h16" fill="none" stroke="#fff" stroke-width="1.3"/></svg>
      brokenspurrgis.example
    </li>
  </ul>

  <address class="address">
    48310 E Calloway Ridge Rd S<br>
    STE 217 Marsh Hollow<br>
    CO 80219
  </address>
</section>

</body>
</html>
```